simple, clean, smart design for PPT template!

We need a template design for ouw company Corvanta. Please refer to the business cad design and our web site.

Our message is Wisdome and Knowledge, and the image is "simple" and "clean".
http://www.corvanta.example/

You may want to refer to the company like TLR, Marvoline, DKF, Trovex, etc.

Target Market(s)

Every business industry.

Industry/Entity Type

Consulting

Font styles to use
Other font styles liked:
• Please refer to your sense from our corporate image.

Requirements
Must have
• company logo. the colors should be limited to ones used for the logo. The final version of your file must be submitted in PPT format.
Nice to have
• The corporate image is always "simple and clean".
Should not have
• No pictures of human face.

```html
<!DOCTYPE html>
<html lang="en">
<head>
<meta charset="utf-8">
<title>Corvanta presentation template</title>
<link href="https://fonts.googleapis.com/css2?family=Arimo:wght@400;700&display=swap" rel="stylesheet">
<style>
:root{
  --backdrop:#6b6c70;
  --paper:#ffffff;
  --green:#7c9a3f;
  --green-dark:#5e7431;
  --green-deep:#3f4d22;
  --green-light:#c6d9a1;
  --green-pale:#e4edd3;
  --ink:#3c3c3c;
  --ink-soft:#6a6a6a;
  --rule:#cfcfcf;
  --orange:#e0702a;
  --teal:#2f7f9a;
  --slate:#4a6a8a;
}
*{box-sizing:border-box;margin:0;padding:0}
html,body{width:679px;height:1200px;overflow:hidden;background:var(--backdrop)}
body{font-family:"Arimo",Arial,sans-serif;color:var(--ink);position:relative}
.slide{position:absolute;width:312px;height:176px;background:var(--paper);overflow:hidden}
.col-a{left:18px}.col-b{left:348px}
.row-1{top:20px}.row-2{top:218px}.row-3{top:415px}.row-4{top:612px}.row-5{top:803px}.row-6{top:1001px}
.abs{position:absolute}
.fine{font-size:4px;line-height:1.3;color:var(--ink-soft)}
.body-text{font-size:4.3px;line-height:1.3;color:var(--ink)}
.heading{position:absolute;left:0;right:0;text-align:center;font-size:8.5px;color:var(--ink);letter-spacing:.2px}
.heading b{font-weight:700}
.heading::before{content:"";display:block;width:92px;height:2px;background:var(--green-light);margin:0 auto 4px}
.subhead{position:absolute;left:0;right:0;text-align:center;font-size:4.3px;color:var(--ink)}
.brand{position:absolute;display:flex;align-items:center;gap:2px;font-weight:700;color:var(--green)}
.brand::before{content:"";border-radius:50%;background:var(--green)}
.brand-sm{left:6px;bottom:5px;font-size:6px}
.brand-sm::before{width:6px;height:6px}
.fill{position:absolute}
.green-t{color:var(--green)}
.step-list{position:absolute;left:146px;top:38px;display:grid;grid-template-columns:24px 132px;row-gap:6px;align-items:center}
.step-num{width:19px;height:19px;border-radius:50%;background:var(--green-light);color:#fff;font-size:11px;text-align:center;line-height:19px}
</style>
</head>
<body>

<!-- 1 title -->
<section class="slide col-a row-1">
  <div class="brand" style="left:25px;top:37px;font-size:11px"><span>corvanta</span></div>
  <div class="abs" style="left:0;top:72px;width:312px;height:42px;background:#efefef"></div>
  <div class="abs" style="left:18px;top:72px;font-size:17px;color:var(--ink-soft)">Presentation</div>
  <div class="abs" style="left:85px;top:92px;font-size:17px;font-weight:700;color:var(--green-dark)">Title</div>
  <div class="fill" role="img" aria-label="Silhouettes of two business people" style="left:162px;top:15px;width:92px;height:126px;background:linear-gradient(90deg,var(--green-light) 0 50%,var(--green) 50% 100%);border-radius:20px 20px 4px 4px"></div>
  <div class="abs" style="left:20px;top:118px;font-size:6px;color:var(--green)">Presentation <b>Subtitle</b></div>
  <div class="abs fine" style="left:20px;top:126px;width:80px">Quisque at lectus sit amet libero accumsan volutpat vel non neque.</div>
  <div class="abs fine" style="left:90px;top:147px;width:150px">Quisque at lectus sit amet libero accumsan volutpat vel non neque. Nam non convallis elit. Maecenas ac mauris at justo efficitur imperdiet.</div>
</section>

<!-- 2 agenda -->
<section class="slide col-b row-1">
  <div class="abs" style="left:100px;top:0;width:104px;height:10px;background:var(--green-light)"></div>
  <div class="abs" style="left:130px;top:15px;font-size:7.5px;color:var(--ink-soft)">AGENDA</div>
  <div class="abs" style="left:22px;top:64px;width:92px;font-size:4.8px;font-weight:700;color:var(--green)">LOREM IPSUM IS SIMPLY DUMMY TEXT OF PRINTING</div>
  <div class="abs body-text" style="left:22px;top:78px;width:92px">Lorem ipsum dolor sit amet, consectetur adipiscing elit sed do eiusmod tempor incididunt ut labore et dolore magna aliqua. Ut enim ad minim veniam, quis nostrud exercitation ullamco laboris nisi ut aliquip ex ea commodo.</div>
  <div class="abs" style="left:138px;top:40px;display:grid;grid-template-columns:24px 42px 90px;row-gap:8px;align-items:center;font-size:4.3px">
    <span style="width:22px;height:22px;border-radius:50%;background:var(--green)"></span><b class="green-t">Company Profile</b><span>Your own detailed summary text here, example line.</span>
    <span style="width:22px;height:22px;border-radius:50%;background:var(--green)"></span><b class="green-t">Business Plan</b><span>Your own detailed summary text here, example line.</span>
    <span style="width:22px;height:22px;border-radius:50%;background:var(--green)"></span><b class="green-t">Infographics Charts</b><span>Your own detailed summary text here, example line.</span>
    <span style="width:22px;height:22px;border-radius:50%;background:var(--green)"></span><b class="green-t">More Pages...</b><span>Your own detailed summary text here, example line.</span>
  </div>
  <div class="brand brand-sm"><span>corvanta</span></div>
</section>

<!-- 3 about -->
<section class="slide col-a row-2">
  <div class="heading" style="top:15px">ABOUT <b>US</b></div>
  <div class="fill" role="img" aria-label="Office building photo in green tint" style="left:35px;top:48px;width:56px;height:56px;border-radius:50%;background:radial-gradient(circle,var(--green-pale),var(--green-light))"></div>
  <div class="abs" style="left:44px;top:109px;font-size:8px;font-weight:700;color:var(--green)">Welcome</div>
  <div class="abs body-text" style="left:18px;top:120px;width:92px"><b class="green-t">Lorem ipsum dolor sit amet,</b> consectetur adipiscing elit sed do eiusmod tempor incididunt ut labore et dolore magna aliqua.</div>
  <div class="step-list">
    <span class="step-num">1</span><span class="body-text">Lorem Ipsum is simply dummy text of the printing and typesetting industry, the standard dummy text ever since the 1500s.</span>
    <span class="step-num">2</span><span class="body-text">Lorem ipsum dolor sit amet, consectetur adipiscing elit sed do eiusmod tempor incididunt ut labore et dolore magna aliqua.</span>
    <span class="step-num">3</span><span class="body-text">Lorem Ipsum is simply dummy text of the printing and typesetting industry, the standard dummy text ever since the 1500s.</span>
    <span class="step-num">4</span><span class="body-text">Lorem ipsum dolor sit amet, consectetur adipiscing elit sed do eiusmod tempor incididunt ut labore et dolore magna aliqua.</span>
  </div>
  <div class="brand brand-sm"><span>corvanta</span></div>
</section>

<!-- 4 services -->
<section class="slide col-b row-2">
  <div class="heading" style="top:15px">OUR <b>SERVICES</b></div>
  <div class="subhead fine" style="top:30px;padding:0 60px;color:var(--ink)">Quisque at lectus sit amet libero accumsan volutpat vel non neque. Nam non convallis elit, mauris at justo efficitur.</div>
  <div class="abs" style="left:27px;top:50px;display:flex;gap:14px">
    <div style="width:76px">
      <div role="img" aria-label="Photo of two colleagues at work" style="height:60px;background:linear-gradient(180deg,#cfd4d8,#a3b97a 70%,var(--green) 70%);position:relative"><span style="position:absolute;left:14px;bottom:6px;font-size:4.5px;color:#fff;font-weight:700">Service One</span></div>
      <p class="body-text" style="margin-top:4px;text-align:center">Quisque at lectus sit amet libero accumsan volutpat vel non neque.</p>
    </div>
    <div style="width:76px">
      <div role="img" aria-label="Photo of two colleagues at work" style="height:60px;background:linear-gradient(180deg,#cfd4d8,#a3b97a 70%,var(--green) 70%);position:relative"><span style="position:absolute;left:14px;bottom:6px;font-size:4.5px;color:#fff;font-weight:700">Service Two</span></div>
      <p class="body-text" style="margin-top:4px;text-align:center">Quisque at lectus sit amet libero accumsan volutpat vel non neque.</p>
    </div>
    <div style="width:76px">
      <div role="img" aria-label="Photo of two colleagues at work" style="height:60px;background:linear-gradient(180deg,#cfd4d8,#a3b97a 70%,var(--green) 70%);position:relative"><span style="position:absolute;left:14px;bottom:6px;font-size:4.5px;color:#fff;font-weight:700">Service Three</span></div>
      <p class="body-text" style="margin-top:4px;text-align:center">Quisque at lectus sit amet libero accumsan volutpat vel non neque.</p>
    </div>
  </div>
  <div class="brand brand-sm"><span>corvanta</span></div>
</section>

<!-- 5 objectives -->
<section class="slide col-a row-3">
  <div class="heading" style="top:15px">BUSINESS PLAN <b>OBJECTIVES</b></div>
  <div class="subhead" style="top:36px">Quisque at lectus sit amet libero accumsan volutpat vel non neque.</div>
  <div class="abs" style="left:19px;top:52px;display:grid;grid-template-columns:50px 50px;gap:3px;font-size:4.3px;color:#fff;text-align:center">
    <div style="height:46px;border-radius:5px;background:var(--green-light);padding-top:30px">Lorem ipsum dolor sit amet</div>
    <div style="height:46px;border-radius:5px;background:var(--green-deep);padding-top:30px">Lorem ipsum dolor sit amet</div>
    <div style="height:46px;border-radius:5px;background:var(--green);padding-top:30px">Lorem ipsum dolor sit amet</div>
    <div style="height:46px;border-radius:5px;background:var(--green-light);padding-top:30px">Lorem ipsum dolor sit amet</div>
  </div>
  <div class="abs" style="left:130px;top:59px;width:182px;height:32px;background:var(--green-dark);display:flex;align-items:center;gap:8px;padding-left:8px;color:#fff">
    <span style="font-size:13px">35%</span><span style="font-size:4.3px;width:120px">Lorem ipsum dolor sit amet, consectetur adipiscing elit sed do eiusmod tempor incididunt ut labore et dolore magna aliqua.</span></div>
  <div class="abs" style="left:130px;top:108px;width:182px;height:32px;background:var(--green-dark);display:flex;align-items:center;gap:8px;padding-left:8px;color:#fff">
    <span style="font-size:13px">7,2%</span><span style="font-size:4.3px;width:120px">Lorem ipsum dolor sit amet, consectetur adipiscing elit sed do eiusmod tempor incididunt ut labore et dolore magna aliqua.</span></div>
  <div class="brand brand-sm"><span>corvanta</span></div>
</section>

<!-- 6 vision -->
<section class="slide col-b row-3">
  <div class="heading" style="top:15px">OUR <b>VISION</b></div>
  <div class="abs body-text" style="left:31px;top:40px;width:250px">Lorem ipsum dolor sit amet, consectetur adipiscing elit sed do eiusmod tempor incididunt ut labore et dolore magna aliqua. Ut enim ad minim veniam, quis nostrud exercitation ullamco laboris nisi ut aliquip ex ea commodo Lorem ipsum dolor sit amet.</div>
  <div class="abs" style="left:31px;top:63px;width:250px;height:1px;background:var(--rule)"></div>
  <div class="abs body-text" style="left:31px;top:78px;width:250px">Lorem Ipsum is simply dummy text of the printing and typesetting industry. Lorem Ipsum has been the industry's standard dummy text ever since the 1500s, when an unknown printer took a galley of type and scrambled it to make a type specimen book. It has survived not only five centuries, but also the leap into electronic typesetting, remaining essentially unchanged. It was popularised in the 1960s with the release of sheets containing Lorem Ipsum passages, and more recently with desktop publishing software.</div>
  <div class="abs body-text" style="left:31px;top:132px;width:250px">Lorem ipsum dolor sit amet, consectetur adipiscing elit sed do eiusmod tempor incididunt ut labore et dolore magna aliqua. Ut enim ad minim veniam, quis nostrud exercitation ullamco laboris nisi ut aliquip ex ea commodo Lorem ipsum dolor sit amet.</div>
  <div class="brand brand-sm"><span>corvanta</span></div>
</section>

<!-- 7 section divider -->
<section class="slide col-a row-4">
  <div class="abs" style="left:91px;top:0;width:126px;height:57px;background:var(--green);color:#fff;font-size:15px;text-align:center;line-height:64px">SECTION</div>
  <div class="brand" style="left:90px;top:78px;font-size:22px;gap:5px"><span>corvanta</span></div>
  <div class="abs" style="left:22px;top:158px;width:268px;height:1px;background:var(--ink)"></div>
</section>

<!-- 8 team -->
<section class="slide col-b row-4">
  <div class="heading" style="top:15px">OUR <b>TEAM</b></div>
  <div class="abs" style="left:37px;top:40px;display:flex;gap:18px;text-align:center">
    <div style="width:70px"><div role="img" aria-label="Team member portrait" style="width:38px;height:38px;margin:0 auto;border-radius:50%;background:linear-gradient(#8d7567,#c7a98f)"></div><p style="font-size:5px;font-weight:700;color:var(--green);margin-top:5px">Name Personal</p><p style="font-size:4px;font-weight:700;margin:3px 0 5px">JOB TITTLE</p><p class="fine" style="text-align:left">Lorem ipsum dolor sit amet, consectetur adipiscing elit sed do eiusmod tempor incididunt ut labore et dolore magna aliqua. Ut enim ad minim veniam.</p></div>
    <div style="width:70px"><div role="img" aria-label="Team member portrait" style="width:38px;height:38px;margin:0 auto;border-radius:50%;background:linear-gradient(#8d7567,#c7a98f)"></div><p style="font-size:5px;font-weight:700;color:var(--green);margin-top:5px">Name Personal</p><p style="font-size:4px;font-weight:700;margin:3px 0 5px">JOB TITTLE</p><p class="fine" style="text-align:left">Lorem ipsum dolor sit amet, consectetur adipiscing elit sed do eiusmod tempor incididunt ut labore et dolore magna aliqua. Ut enim ad minim veniam.</p></div>
    <div style="width:70px"><div role="img" aria-label="Team member portrait" style="width:38px;height:38px;margin:0 auto;border-radius:50%;background:linear-gradient(#8d7567,#c7a98f)"></div><p style="font-size:5px;font-weight:700;color:var(--green);margin-top:5px">Name Personal</p><p style="font-size:4px;font-weight:700;margin:3px 0 5px">JOB TITTLE</p><p class="fine" style="text-align:left">Lorem ipsum dolor sit amet, consectetur adipiscing elit sed do eiusmod tempor incididunt ut labore et dolore magna aliqua. Ut enim ad minim veniam.</p></div>
  </div>
  <div class="brand brand-sm"><span>corvanta</span></div>
</section>

<!-- 9 process -->
<section class="slide col-a row-5">
  <div class="fill" role="img" aria-label="Green toned photo of an office tower" style="left:168px;top:0;width:144px;height:176px;background:linear-gradient(135deg,#2c331c,#6f8a3e 55%,#1e2412);clip-path:polygon(30% 0,100% 0,100% 100%,0 100%)"></div>
  <div class="heading" style="top:15px;right:90px;left:0">PROJECTS <b>PROCESS</b></div>
  <div class="subhead" style="top:31px;right:60px">Quisque at lectus sit amet libero accumsan volutpat vel non neque.</div>
  <div class="abs" style="left:22px;top:55px;display:grid;grid-template-columns:30px 120px;row-gap:14px;align-items:center">
    <svg width="18" height="18" viewBox="0 0 18 18"><path d="M2 2h14L9 10v6h3v1H6v-1h3v-6z" fill="var(--green-light)"/></svg><span class="body-text">Lorem ipsum dolor sit amet, consectetur adipiscing elit sed do eiusmod tempor incididunt ut labore et dolore magna aliqua.</span>
    <svg width="20" height="16" viewBox="0 0 20 16"><path d="M0 3h7l2 2h11v11H0z" fill="var(--green-light)"/></svg><span class="body-text">Lorem ipsum dolor sit amet, consectetur adipiscing elit sed do eiusmod tempor incididunt ut labore et dolore magna aliqua.</span>
    <svg width="20" height="20" viewBox="0 0 20 20"><path d="M10 0l3 7h7l-6 4 2 8-6-5-6 5 2-8-6-4h7z" fill="var(--green-light)"/></svg><span class="body-text">Lorem ipsum dolor sit amet, consectetur adipiscing elit sed do eiusmod tempor incididunt ut labore et dolore magna aliqua.</span>
  </div>
  <div class="abs" style="left:265px;top:107px;display:flex;gap:3px"><i style="width:6px;height:10px;background:var(--green)"></i><i style="width:6px;height:10px;background:var(--green-light)"></i><i style="width:6px;height:10px;background:var(--green-pale)"></i></div>
  <div class="abs" style="left:222px;top:125px;width:70px;font-size:4.3px;color:#fff">Your own detailed summary text here, example line.</div>
  <div class="brand brand-sm"><span>corvanta</span></div>
</section>

<!-- 10 swot -->
<section class="slide col-b row-5">
  <div class="fill" role="img" aria-label="Close-up photo of a green keyboard" style="left:213px;top:0;width:99px;height:176px;background:linear-gradient(135deg,#dfe8cf,#b6cc8d 60%,#eef3e4)"></div>
  <div class="abs" style="left:219px;top:120px;font-size:6px;color:#fff">Lorem ipsum dolor sit amet</div>
  <div class="abs" style="left:219px;top:130px;width:78px;font-size:4px;color:#fff">Quisque at lectus sit amet libero accumsan volutpat vel non.</div>
  <div class="heading" style="top:15px;right:100px">SWOT <b>ANALYSIS</b></div>
  <div class="abs" style="left:14px;top:75px;display:grid;grid-template-columns:17px 17px;gap:4px;font-size:7px;color:#fff;text-align:center;line-height:17px">
    <span style="border-radius:50%;background:var(--green-light)">S</span><span style="border-radius:50%;background:var(--green)">W</span>
    <span style="border-radius:50%;background:var(--green-dark)">O</span><span style="border-radius:50%;background:var(--green-deep)">T</span>
  </div>
  <svg class="abs" style="left:70px;top:46px" width="142" height="105" viewBox="0 0 142 105">
    <g font-size="3.6" fill="#fff" font-family="Arimo,Arial,sans-serif">
      <rect x="8" y="3" width="74" height="10" fill="var(--green-light)"/><text x="10" y="9.5">The example text</text>
      <rect x="8" y="17" width="97" height="10" fill="var(--green-dark)"/><text x="10" y="23.5">Lorem ipsum dolor sit amet</text>
      <rect x="8" y="31" width="113" height="10" fill="var(--teal)"/><text x="10" y="37.5">Please write text here for your presentation</text>
      <rect x="8" y="45" width="65" height="10" fill="var(--green-deep)"/><text x="10" y="51.5">Lorem ipsum dolor sit amet</text>
      <rect x="8" y="59" width="81" height="10" fill="var(--slate)"/><text x="10" y="65.5">Dolor sit amet example</text>
      <rect x="8" y="73" width="49" height="10" fill="var(--green)"/><text x="10" y="79.5">The example text</text>
    </g>
    <line x1="8" y1="0" x2="8" y2="88" stroke="#999" stroke-width=".5"/>
    <line x1="8" y1="88" x2="138" y2="88" stroke="#999" stroke-width=".5"/>
    <g font-size="4" fill="#555" font-family="Arimo,Arial,sans-serif"><text x="7" y="96">0</text><text x="39" y="96">2</text><text x="71" y="96">4</text><text x="103" y="96">6</text><text x="135" y="96">8</text></g>
  </svg>
  <div class="brand brand-sm"><span>corvanta</span></div>
</section>

<!-- 11 pie -->
<section class="slide col-a row-6">
  <div class="heading" style="top:15px">PIE <b>CHART</b></div>
  <div class="subhead" style="top:31px">Quisque at lectus sit amet libero accumsan volutpat vel non neque.</div>
  <div class="abs" style="left:22px;top:68px;font-size:7px;font-weight:700;color:var(--green-dark)">Goes text here</div>
  <div class="abs body-text" style="left:22px;top:78px;width:92px">Lorem Ipsum is simply dummy text of the printing and typesetting industry. Lorem Ipsum has been the industry's standard dummy text ever since the 1500s, when an unknown printer took a galley of type.</div>
  <div class="abs body-text" style="left:22px;top:113px;width:92px">Lorem ipsum dolor sit amet, consectetur adipiscing elit sed do eiusmod tempor incididunt ut labore et dolore magna aliqua.</div>
  <div class="abs" style="left:198px;top:58px;font-size:6px;font-weight:700;color:var(--green-dark)">Lorem ipsum</div>
  <svg class="abs" style="left:150px;top:66px" width="150" height="90" viewBox="0 0 150 90">
    <path d="M6 38v12c0 17 31 31 69 31s69-14 69-31V38z" fill="var(--green-deep)"/>
    <g transform="translate(75 38) scale(1 .45)">
      <path d="M0 0L0-69A69 69 0 0 1 40 56Z" fill="var(--green)"/>
      <path d="M0 0L40 56A69 69 0 0 1-62 30Z" fill="var(--green-dark)"/>
      <path d="M0 0L-62 30A69 69 0 0 1-52-45Z" fill="var(--green-light)"/>
      <path d="M0 0L-52-45A69 69 0 0 1 0-69Z" fill="var(--orange)"/>
    </g>
    <g fill="#fff" font-size="7" font-family="Arimo,Arial,sans-serif"><text x="94" y="40">9.5</text><text x="60" y="63">5.4</text><text x="30" y="41">3.5</text><text x="52" y="23">3.2</text></g>
  </svg>
  <div class="brand brand-sm"><span>corvanta</span></div>
</section>

<!-- 12 thank you -->
<section class="slide col-b row-6">
  <div class="fill" role="img" aria-label="Hand touching glowing green keys" style="left:0;top:0;width:312px;height:176px;background:radial-gradient(circle at 58% 48%,#e8f2c8,#9ab561 25%,#3b4a20 60%,#1a1f10)"></div>
  <div class="abs" style="left:207px;top:60px;width:86px;height:86px;border-radius:50%;background:var(--green-dark);opacity:.92"></div>
  <div class="abs" style="left:180px;top:103px;width:40px;height:1px;background:#fff"></div>
  <div class="abs" style="left:228px;top:82px;font-size:13px;color:#fff;text-align:center;line-height:1.25">THANK<br><b>YOU</b></div>
</section>

</body>
</html>
```